Client Publishing Agency Brochure

We need a company brochure for a new company based in Cape Town, South Africa called Willowmere Lantern Studio (WLS).

We need a brochure marketing our publishing agency (wls:scribe) and our creative, interactive & print production division (wls:forge). Develop a fresh design concept which will direct the design of our new website in the near future. (So don't pay attention to our current web page. It does not reflect our brand).

wls:scribe is a content marketing agency offering our clients (B2B, B2C, NPO, Professional & Membership Organizations) branded publishing to build trust, authority and relationships with their customers. A typical content strategy may include communication through client print or online magazine, newsletters, microsite, website, social technology and plenty more). We want to communicate that company's need to change their mind set from promoting their products and begin to invest in developing a relationship with their potential & existing customers. The drive is a Return On Objectives (business & marketing objectives) and interest is a Return On Investment (ROI).

wls:forge is a creative, interactive & print production agency which supports our client's marketing collateral needs.
Updates

Hi Designers,

This is a response to questions posted earlier to assist you in your project.

Q.What will the size of brochure be?
A. A4 size with folder flap for the back cover

Q.Will it be a three panels double sided?
A. Depends on your creative concept. But if you make a 3 panel dbl side then layout two version for print (double sided 3 panel) and digital pdf (single pdf pages in sequence).

Q.The images that you supplied I know are just samples, What type of images are 
required? 
A. Depends on your creative concept. Let the style of the logo inspire you. What I liked in the examples is the classic, premium, quality feel. So no business stock imagery. I'm also a creative agency so that message needs to come through. Illustrated styles are welcome.

Q.Should design have same feel as your website? 
A. No. Our website is pending the outcome of the brochure. The brochure will be our creative direction for our new website. So creative an inspiring and clean brochure.

Please feel free to post additional questions. Good Luck and thank you for your participation.

Reason: The designers have not produced a style and concept that reflects our brand. Would like to guide them more to reach the right look for our company.

Hi Designers...

I have not been happy with the quality of ideas and execution of those ideas. This I understand could a combination of a poor brief and a non-guarenteed project.

I have rectified the brief and have guaranteed the award. Please don't hold back on your creativity and return the guarantee for high quality.

Please ask me any questions to better understand what we are looking for.

Remember. This brochure is a new design concept. Do not visit the web page for inspiration. The new design concept for the brochure will set the tone and inspire a new website.

Lets create a beautiful product together.

Thank you for your participation.

Reason: Designers are not following the brief, and not respecting the logo and colour policies/guidelines and those who are submitting work are not asking questions throughout the process to get a better understanding of what we need. All design submissions are always at the last minute. And some designers are are not real designers and using web development software to produce print designs. More importantly after taking time to advise designers of changes, no effort is made by designers to make changes. Each designer submits 1 idea and think that they are going to win the lottery. Where is the work ethic and quality of service? Where are the submissions from the designers who accepted the participation fee? There were a few designers who promised participation and never showed up. Maybe it all our fault? But we not happy with the service and level of creativity. Not sure if these designers are taking pride in their work or not. I know a few of you are.

Target Market(s)

B2B, B2C, NPO, Professional & Membership Organizations - Make up professionals and decision makers across sectors from Shipping and Logistics, Manufacturing, Legal to Art & Culture.

Industry/Entity Type

Communication

Requirements
Must have
• Size: A4
x 2 Panels
+ Folder flap (for A4 Paper, business card slot)
Styled map to our premises. See map attachment for example.

Pages: 10 including cover (if you need more than this let your design motivate the need for more pages)

(See logo use eps file)
(See colour use eps file)

Nice to have
• Styled map to our premises. See attachment for example.
Should not have
• Do not take any inspiration from our website. It is just a free template to show customers that it is still under construction.

Do not include stock symbols and typical business stock images. Remember we are a creative offering, so our brochure should show originality, innovation and individuality.

```html
<!DOCTYPE html>
<html lang="en">
<head>
<meta charset="utf-8">
<title>WLS – Who we are</title>
<link rel="stylesheet" href="https://fonts.googleapis.com/css2?family=Source+Sans+3:wght@400;600;700&display=swap">
<style>
  :root {
    --page-dark: #a9a9a9;
    --page-mid: #c4c4c4;
    --page-light: #e2e2e2;
    --ink: #1a1a1a;
    --panel: #e3e3e3;
    --tab: #ffe08a;
    --band: #ffc21a;
    --band-end: #ff9f1a;
    --black: #000000;
    --white: #ffffff;
    --dot-red: #ef3b4f;
    --dot-green: #5cbf3a;
    --dot-blue: #4db4ec;
    --dot-orange: #f7941d;
    --dot-violet: #8e6bbf;
  }
  * { box-sizing: border-box; margin: 0; padding: 0; }
  html, body { width: 847px; height: 1200px; overflow: hidden; }
  body { font-family: "Source Sans 3", "Myriad Pro", sans-serif; color: var(--ink); }

  .page {
    position: relative;
    width: 847px;
    height: 1200px;
    overflow: hidden;
    background: linear-gradient(160deg, var(--page-dark) 0%, var(--page-mid) 35%, var(--page-mid) 60%, var(--page-light) 100%);
  }

  .wave-texture {
    position: absolute;
    right: 0; top: 0;
    width: 560px; height: 1200px;
    background: radial-gradient(ellipse at 70% 55%, rgba(255,255,255,0.45) 0%, rgba(255,255,255,0.15) 45%, rgba(255,255,255,0) 75%);
  }

  .brand {
    position: absolute;
    left: 78px; top: 116px;
    display: flex; align-items: center; gap: 12px;
  }
  .brand-name {
    font-size: 58px; font-weight: 700; line-height: 1;
    color: var(--ink); letter-spacing: 2px;
  }
  .brand-mark { width: 16px; height: 16px; background: var(--ink); }

  .section-title {
    position: absolute;
    left: 275px; top: 107px;
    width: 213px; height: 77px;
    background: var(--black);
    color: var(--white);
    font-size: 21px; font-weight: 400;
    padding: 26px 0 0 60px;
  }

  .service-band {
    position: absolute;
    left: 74px; top: 247px;
    width: 600px; height: 26px;
    background: linear-gradient(90deg, var(--band) 0%, var(--band) 80%, var(--band-end) 100%);
  }
  .dot-strip {
    position: absolute;
    background: linear-gradient(90deg, var(--dot-red), var(--dot-orange), var(--dot-green), var(--dot-blue), var(--dot-violet), var(--dot-red));
    opacity: 0.75;
  }
  .dot-strip.top { left: 643px; top: 245px; width: 161px; height: 26px; }
  .dot-strip.bottom { left: 367px; top: 1109px; width: 368px; height: 30px; }

  .services {
    position: absolute;
    left: 85px; top: 249px;
    display: flex; gap: 11px;
  }
  .service {
    width: 160px; height: 242px;
    background: var(--panel);
  }
  .service h2 {
    height: 24px;
    background: var(--tab);
    font-size: 19px; font-weight: 600; line-height: 24px;
    padding-left: 10px;
  }
  .service ul {
    list-style: none;
    padding: 10px 0 0 10px;
    font-size: 13.5px; line-height: 30px;
  }

  .intro {
    position: absolute;
    left: 72px; top: 506px;
    width: 640px;
    font-size: 16.3px; line-height: 30px;
  }
  .intro p + p { margin-top: 30px; }

  .page-number {
    position: absolute;
    left: 740px; top: 1113px;
    width: 26px; height: 26px;
    background: var(--black); color: var(--white);
    font-size: 12px; font-weight: 700;
    text-align: center; line-height: 26px;
  }
</style>
</head>
<body>
  <div class="page">
    <div class="wave-texture" role="img" aria-label="Soft flowing white line pattern sweeping down the right side of the page"></div>

    <div class="brand">
      <span class="brand-name">WLS</span>
      <span class="brand-mark"></span>
    </div>

    <div class="section-title">Who we are</div>

    <div class="service-band"></div>
    <div class="dot-strip top" role="img" aria-label="Rows of small multicoloured squares"></div>

    <div class="services">
      <section class="service">
        <h2>Print</h2>
        <ul>
          <li>Magazines</li>
          <li>Supplements</li>
          <li>Brochures</li>
          <li>Catalogues</li>
          <li>Books</li>
          <li>Leaflets</li>
          <li>Branding</li>
        </ul>
      </section>
      <section class="service">
        <h2>Digital</h2>
        <ul>
          <li>Online magazines</li>
          <li>Emails/eDM</li>
          <li>E-content</li>
          <li>Social media</li>
          <li>Mobile</li>
          <li>Website development</li>
        </ul>
      </section>
      <section class="service">
        <h2>Commercial</h2>
        <ul>
          <li>Advertising media sales</li>
          <li>Commercial</li>
          <li>partnerships</li>
          <li>Competitions</li>
          <li>Promotions and offers</li>
        </ul>
      </section>
    </div>

    <div class="intro">
      <p>Client magazines<br>
      Client magazines are measurably more effective than traditional marketing channels<br>
      at simultaneously building brand awareness, driving sales and generating loyalty<br>
      through meaningful engagement.</p>
      <p>We combine our team’s journalistic expertise and<br>
      provoking design ideas with subject specialists in your industry to produce content<br>
      that interests, informs and educates your audience. As a result your branded magazine<br>
      offers authentic value to readers, achieves ROO, and illuminates your brand colours<br>
      in your market.</p>
      <p>Our commercial services offer an opportunity of leveraging off advertising and<br>
      sponsorship, considerably reducing project costs while helping your business<br>
      audience increase marketing effectiveness.</p>
    </div>

    <div class="dot-strip bottom" role="img" aria-label="Rows of small multicoloured squares"></div>
    <div class="page-number">4</div>
  </div>
</body>
</html>
```